Mara Penwick Concert Poster

I am a fulltime Christian singer from NZ. I need a new Concert Poster.
Specs: Color pic supplied but prefer b&w. Portrait orientation, not landscape. Copy supplied (to appear on bottom half of poster). Need blank box or strip near bottom for local venue details. Signature-style 'Mara Penwick' title across the photo or across the top, but totally open to design ideas/suggestion.

Target Market(s)

Mainly churches where I sing..

Industry/Entity Type

Singer

Requirements
Must have
• From past experience I have found a dark (even black) background, has most impact, with copy reversed out.. But as above, I am open to suggestions re color and feel. View my music on Vidorra for additional feel ideas.
Nice to have
• Simple direct classy style best, with minimal clutter.

```html
<!DOCTYPE html>
<html lang="en">
<head>
<meta charset="utf-8">
<title>Mara Penwick Concert Poster</title>
<link rel="stylesheet" href="https://fonts.googleapis.com/css2?family=Great+Vibes&family=Lora:ital,wght@1,400;1,700&family=Open+Sans:wght@400;700&display=swap">
<style>
  :root {
    --ink: #000000;
    --paper: #ffffff;
    --text-dark: #1a1a1a;
    --photo-light: #8a8a8a;
    --photo-mid: #4a4a4a;
    --photo-dark: #141414;
  }
  * { margin: 0; padding: 0; box-sizing: border-box; }
  html, body {
    width: 684px;
    height: 1200px;
    overflow: hidden;
    background: var(--paper);
  }
  .poster {
    position: relative;
    width: 684px;
    height: 1200px;
    background: var(--paper);
    overflow: hidden;
  }
  .hero-photo {
    position: absolute;
    left: 0; top: 0;
    width: 684px;
    height: 585px;
    background:
      radial-gradient(ellipse 260px 230px at 420px 300px, var(--photo-light) 0%, rgba(110,110,110,0.4) 55%, transparent 100%),
      radial-gradient(ellipse 400px 200px at 520px 80px, rgba(160,160,160,0.55) 0%, transparent 70%),
      radial-gradient(ellipse 220px 300px at 120px 420px, rgba(60,60,60,0.9) 0%, transparent 80%),
      linear-gradient(180deg, var(--photo-mid) 0%, var(--photo-dark) 100%);
  }
  .artist-name {
    position: absolute;
    top: 8px;
    left: 0;
    width: 100%;
    text-align: center;
    font-family: "Great Vibes", cursive;
    font-size: 104px;
    line-height: 1.1;
    color: var(--paper);
    text-shadow: 0 2px 6px rgba(0,0,0,0.5);
  }
  .quote-band {
    position: absolute;
    left: 0; top: 585px;
    width: 684px;
    height: 190px;
    background: var(--ink);
    color: var(--paper);
    text-align: center;
    padding-top: 28px;
  }
  .quote-text {
    font-family: "Lora", Georgia, serif;
    font-style: italic;
    font-size: 29px;
    line-height: 1.42;
  }
  .quote-source {
    margin-top: 12px;
    font-family: "Lora", Georgia, serif;
    font-style: italic;
    font-weight: 700;
    font-size: 16px;
  }
  .credentials {
    position: absolute;
    top: 800px;
    left: 0;
    width: 100%;
    text-align: center;
    font-family: "Open Sans", Arial, sans-serif;
    font-size: 16px;
    line-height: 1.5;
    color: var(--text-dark);
  }
  .credentials strong { font-weight: 700; }
  .venue-space {
    position: absolute;
    top: 900px;
    left: 0;
    width: 100%;
    height: 200px;
  }
  .divider {
    position: absolute;
    top: 1121px;
    left: 278px;
    width: 128px;
    height: 3px;
    background: var(--ink);
  }
  .tour-info {
    position: absolute;
    top: 1146px;
    left: 0;
    width: 100%;
    text-align: center;
    font-family: "Open Sans", Arial, sans-serif;
    font-size: 16px;
    color: var(--text-dark);
    letter-spacing: 0.3px;
  }
</style>
</head>
<body>
  <main class="poster">
    <div class="hero-photo" role="img" aria-label="Black and white portrait of the singer holding an acoustic guitar against a dramatic cloudy sky"></div>
    <h1 class="artist-name">Mara Penwick</h1>

    <section class="quote-band">
      <p class="quote-text">“ There is a depth in your songs that is<br>very rare in Christian music today ”</p>
      <p class="quote-source">Vidorra comment Aug 10, 2011</p>
    </section>

    <section class="credentials">
      <p>New Zealand's most prolific and accomplished</p>
      <p>Christian singer/songwriter</p>
      <p><strong>12 albums, 3 Gold Albums, 2 NZ Music Awards</strong></p>
    </section>

    <div class="venue-space" aria-label="Space for local venue details"></div>

    <div class="divider"></div>
    <p class="tour-info">Tour Schedule &amp; Info:&nbsp; www.marapenwick.com</p>
  </main>
</body>
</html>
```